To revamp the exting web page and Company presentation to new propsective client

We are company establish in 2006. We have a combine of Veltrix implementation team of more than 10 years. We focus on the following areas

a) Veltrix T-ledger range implementation
b) Veltrix T-ledger range platform migration
c) Large database size in excess of 20TB

We need to redesign a our existing new card to give a new look and refresh look. Kindly visit our website for more info www.bnlzq.com

Your main them is blue color and hope to hear from you all.

Target Market(s)

Professional clients

Industry/Entity Type

Information Technology

Contact Information for Business Card

To market our as the leading Veltrix partner in Veltrix t-ledger range implementation

Number of Pages Required

1 page

Colors
3276b5
9bcb3c
cadf82
33a6d7

Requirements
Must have
• The ability to attract new customer and show a level of professionalism.
• You can also add a green color to represent green and environmental friendly.
Nice to have
• To give a total new fresh look for the company
Should not have
• None

```html
<!DOCTYPE html>
<html lang="en">
<head>
<meta charset="UTF-8">
<title>Norvane Commerce Systems – Business Card</title>
<link href="https://fonts.googleapis.com/css2?family=Open+Sans:wght@400;600&family=Orbitron:wght@600&family=Arimo:wght@700&display=swap" rel="stylesheet">
<style>
  :root {
    --backdrop: #262626;
    --card: #ffffff;
    --ink: #333333;
    --muted: #555555;
    --navy: #1f3d6e;
    --brand: #2a2350;
    --accent: #33a6d7;
    --badge: #e0262b;
  }
  * { margin: 0; padding: 0; box-sizing: border-box; }
  html, body { width: 1200px; height: 1000px; overflow: hidden; }
  body { background: var(--backdrop); font-family: "Open Sans", sans-serif; position: relative; }

  .card {
    position: absolute;
    width: 580px; height: 330px;
    background: var(--card);
    border-radius: 26px;
    overflow: hidden;
  }
  .card--front { left: 60px; top: 110px; }
  .card--back { left: 560px; top: 560px; }

  .brand { display: flex; align-items: center; gap: 12px; }
  .brand__dot { width: 30px; height: 30px; border-radius: 50%; background: var(--brand); }
  .brand__text { display: flex; flex-direction: column; }
  .brand__name {
    font-family: "Orbitron", sans-serif; font-weight: 600;
    color: var(--brand); letter-spacing: 8px;
  }
  .brand__tag { font-size: 9px; letter-spacing: 2.5px; color: var(--muted); text-align: right; }

  .card--front .brand { position: absolute; left: 135px; top: 120px; }
  .card--front .brand__name { font-size: 40px; }
  .front__web {
    position: absolute; left: 0; right: 0; bottom: 52px;
    display: flex; justify-content: center; align-items: center; gap: 6px;
    font-size: 15px; color: var(--muted);
  }
  .front__web svg { width: 13px; height: 13px; }

  .card--back .brand { position: absolute; right: 40px; top: 30px; }
  .card--back .brand__dot { width: 22px; height: 22px; }
  .card--back .brand__name { font-size: 28px; letter-spacing: 6px; }
  .card--back .brand__tag { font-size: 7px; letter-spacing: 2px; }

  .back__edge {
    position: absolute; left: 0; right: 0; bottom: 0; height: 10px; background: var(--navy);
  }
  .back__edge--side { left: 0; top: 96px; bottom: auto; width: 5px; height: 40px; }

  .person { position: absolute; left: 36px; top: 84px; }
  .person__name {
    font-family: "Arimo", sans-serif; font-weight: 700;
    font-size: 30px; line-height: 36px; letter-spacing: 3px; color: var(--ink);
  }
  .person__role { font-size: 15px; line-height: 20px; font-weight: 600; color: var(--navy); margin-top: 2px; }

  .contacts { position: absolute; left: 36px; top: 160px; list-style: none; }
  .contacts li {
    display: flex; align-items: center; gap: 10px;
    font-size: 13.5px; color: var(--muted); line-height: 18px;
  }
  .contacts svg { width: 12px; height: 12px; fill: var(--navy); flex: none; }
  .contacts .loc { color: var(--navy); }

  .address { position: absolute; left: 36px; top: 258px; font-size: 13px; color: var(--muted); line-height: 16px; }
  .address__label { font-weight: 600; color: var(--ink); }

  .partner-badge {
    position: absolute; right: 44px; top: 196px;
    width: 70px; height: 26px; background: var(--badge);
  }
</style>
</head>
<body>

<section class="card card--front">
  <div class="brand">
    <span class="brand__dot"></span>
    <div class="brand__text">
      <span class="brand__name">NORVANE</span>
      <span class="brand__tag">Commerce Systems Sdn Bhd</span>
    </div>
  </div>
  <div class="front__web">
    <svg viewBox="0 0 12 12"><circle cx="6" cy="6" r="5.5" fill="#3a4f86"/><path d="M0.5 6h11M6 0.5v11M2 3h8M2 9h8" stroke="#fff" stroke-width="0.7"/></svg>
    <span>www.bnlzq.com</span>
  </div>
</section>

<section class="card card--back">
  <div class="brand">
    <span class="brand__dot"></span>
    <div class="brand__text">
      <span class="brand__name">NORVANE</span>
      <span class="brand__tag">Commerce Systems Sdn Bhd</span>
    </div>
  </div>

  <div class="person">
    <h1 class="person__name">DANIEL KOH</h1>
    <p class="person__role">Chief Operating Officer</p>
  </div>

  <ul class="contacts">
    <li><svg viewBox="0 0 12 12"><path d="M3 1l2 2.5-1 1.5c.8 1.5 1.7 2.4 3 3l1.5-1 2.5 2-1.5 2C5 10.5 1.5 7 1 2.5z"/></svg>60 3 5510 7342</li>
    <li><svg viewBox="0 0 12 12"><path d="M3 1l2 2.5-1 1.5c.8 1.5 1.7 2.4 3 3l1.5-1 2.5 2-1.5 2C5 10.5 1.5 7 1 2.5z"/></svg>65 6218 0937 <span class="loc">(Singapore)</span></li>
    <li><svg viewBox="0 0 12 12"><path d="M3 0h6v12H3zM4 1.5v8h4v-8z" fill-rule="evenodd"/></svg>60 12 845 2261</li>
    <li><svg viewBox="0 0 12 12"><path d="M3 1h6v3H3zM1 4h10v6H1zM3 7h6v4H3z"/></svg>60 3 5510 7300</li>
    <li><svg viewBox="0 0 12 12"><path d="M0 2h12v8H0zM0.8 2.5L6 6.5l5.2-4" stroke="#fff" stroke-width="0.8"/></svg>danielkoh@bnlzq.com</li>
  </ul>

  <div class="address">
    <p class="address__label">Address:</p>
    <p>Suite 6.02, 6th Floor, Wisma Halcyon, Jalan Teratai Indah,</p>
    <p>50480 Kuala Lumpur, Malaysia</p>
  </div>

  <div class="partner-badge" role="img" aria-label="Veltrix partner badge"></div>

  <div class="back__edge"></div>
  <div class="back__edge back__edge--side"></div>
</section>

</body>
</html>
```